Architecture firm needing a business card

We need a business card design for a new company based in the US called "Dorrance Architecture". Seeking minimalist designs that have a creativity/design feel but must be clean and professional. Please refer to the logo attached.

Target Market(s)

Real Estate Investors, Home Builders and Construction Firms.

Industry/Entity Type

Architecture

Contact Information for Business Card

Standard US size business cards. Would like to have some sort of graphic on the back side of the card - nothing that is too loud but something that may catch your attention. More or less grayscale colors that are in line with the logo colors (navy and greys essentially). Additional colors maybe accepted if blended properly (earthtones), but might be difficult to accomplish and maintain the clean/minimalist look.

Requirements
Must have
• Clean Lines
Nice to have
• some sort of graphics, would like to have something creative on the back side of the card
Should not have
• nothing too busy, cluttered or overwhelming.

```html
<!DOCTYPE html>
<html lang="en">
<head>
<meta charset="utf-8">
<title>Dorrance Architecture – Business Card</title>
<link rel="stylesheet" href="https://fonts.googleapis.com/css2?family=Source+Sans+3:wght@400;600&display=swap">
<style>
  :root {
    --stage: #1c1c1e;
    --paper: #f6f6f6;
    --paper-edge: #e4e4e4;
    --navy: #2b4f7a;
    --navy-deep: #1f3e63;
    --navy-light: #4a6f98;
    --rule: #8a9cb8;
    --ink: #2a2a2a;
    --silver: #c9cfd8;
  }
  * { box-sizing: border-box; margin: 0; padding: 0; }
  html, body {
    width: 1200px; height: 864px; overflow: hidden;
    background: var(--stage);
    font-family: "Source Sans 3", "Myriad Pro", Arial, sans-serif;
  }
  .stage {
    position: relative; width: 1200px; height: 864px;
    display: flex; align-items: center; justify-content: center; gap: 48px;
  }
  .card {
    position: relative; width: 525px; height: 300px;
    border-radius: 3px; overflow: hidden;
    box-shadow: 0 10px 30px rgba(0,0,0,.5);
  }
  /* Front */
  .card--front { background: linear-gradient(160deg, #ffffff 0%, var(--paper) 60%, var(--paper-edge) 100%); }
  .front__rule {
    position: absolute; left: 0; right: 0; top: 118px; height: 1px; background: var(--rule);
  }
  .brand {
    position: absolute; display: flex; align-items: center; gap: 12px;
  }
  .brand__mark { width: 30px; height: 30px; flex: none; }
  .brand__name {
    font-weight: 400; text-transform: uppercase; line-height: 1;
  }
  .brand__name span { display: block; }
  .card--front .brand {
    left: 34px; top: 96px; padding: 0 14px 0 10px;
    background: #fbfbfb;
  }
  .card--front .brand__mark { background: var(--navy); }
  .card--front .brand__name { color: var(--navy); font-size: 26px; letter-spacing: 1px; }
  .card--front .brand__name span + span { font-size: 13px; letter-spacing: 3.4px; margin-top: 3px; }

  .contact {
    position: absolute; left: 318px; top: 92px; color: var(--ink);
  }
  .contact__person {
    background: #f7f7f7; padding-right: 8px; margin-bottom: 14px;
  }
  .contact__name {
    color: var(--navy); font-size: 13px; letter-spacing: .6px; text-transform: uppercase; line-height: 1.2;
  }
  .contact__role { font-size: 12px; line-height: 1.2; }
  .contact__list { list-style: none; }
  .contact__item {
    display: flex; align-items: center; gap: 8px;
    font-size: 13px; line-height: 17px; margin-bottom: 2px;
  }
  .contact__icon { width: 13px; height: 13px; flex: none; }
  .contact__address { font-size: 13px; line-height: 17px; margin-top: 8px; }

  /* Back */
  .card--back {
    background: linear-gradient(200deg, var(--navy-deep) 0%, var(--navy) 45%, var(--navy-light) 100%);
    display: flex; align-items: center; justify-content: center;
  }
  .card--back .brand { position: static; }
  .card--back .brand__mark { width: 40px; height: 40px; background: var(--silver); }
  .card--back .brand__name { color: var(--silver); font-size: 34px; letter-spacing: 1px; }
  .card--back .brand__name span + span { font-size: 16px; letter-spacing: 4.6px; margin-top: 4px; }
</style>
</head>
<body>
<main class="stage">
  <section class="card card--front" aria-label="Card front">
    <div class="front__rule"></div>
    <div class="brand">
      <div class="brand__mark"></div>
      <div class="brand__name"><span>Dorrance</span><span>Architecture</span></div>
    </div>
    <div class="contact">
      <div class="contact__person">
        <p class="contact__name">Marian Holloway</p>
        <p class="contact__role">Director</p>
      </div>
      <ul class="contact__list">
        <li class="contact__item">
          <svg class="contact__icon" viewBox="0 0 14 14" aria-hidden="true"><rect width="14" height="14" rx="3" fill="var(--navy)"/><path d="M4.5 3.2l1.4 1.9-.8 1c.5 1 1.3 1.8 2.3 2.3l1-.8 1.9 1.4-.6 1.4c-3.4-.3-6.3-3.2-6.6-6.6z" fill="#fff"/></svg>
          <span>(0000) 555 014</span>
        </li>
        <li class="contact__item">
          <svg class="contact__icon" viewBox="0 0 14 14" aria-hidden="true"><rect width="14" height="14" rx="3" fill="var(--navy)"/><rect x="3" y="4.2" width="8" height="5.6" fill="none" stroke="#fff" stroke-width="1"/><path d="M3 4.4l4 3 4-3" fill="none" stroke="#fff" stroke-width="1"/></svg>
          <span>hello@dorrancearch.com</span>
        </li>
        <li class="contact__item">
          <svg class="contact__icon" viewBox="0 0 14 14" aria-hidden="true"><rect width="14" height="14" rx="3" fill="var(--navy)"/><circle cx="7" cy="7" r="3.8" fill="none" stroke="#fff" stroke-width="1"/><ellipse cx="7" cy="7" rx="1.6" ry="3.8" fill="none" stroke="#fff" stroke-width=".8"/><path d="M3.2 7h7.6" stroke="#fff" stroke-width=".8"/></svg>
          <span>www.dorrancearch.com</span>
        </li>
      </ul>
      <p class="contact__address">214 Cedar Ridge Road<br>Marlow, VA 22810</p>
    </div>
  </section>

  <section class="card card--back" aria-label="Card back">
    <div class="brand">
      <div class="brand__mark"></div>
      <div class="brand__name"><span>Dorrance</span><span>Architecture</span></div>
    </div>
  </section>
</main>
</body>
</html>
```